Design concept for BrightKestrel.com Support Page

We are about to launch a new support page for our www.brightkestrel.com service for photographers and visual artists. The service provides media management, cloud storage, promotional and secure distribution to our members.

The support page will include FAQs and video tutorials.

In particular we're looking for a header for this page that suggests the user is in the support area of our service - so perhaps an illustration that suggests support could look nice (perhaps repair man or doctor iconography). Something to give this area of our site a different look and something that looks both cool and friendly.

Currently the page looks distinctly sparse and undesigned (see attached screenshot) - something that could be remedied, we feel, by some subtle design enhancements that we can implement using CSS.

```html
<!DOCTYPE html>
<html lang="en">
<head>
<meta charset="utf-8">
<title>BrightKestrel Support Center</title>
<link rel="stylesheet" href="https://fonts.googleapis.com/css2?family=Figtree:wght@400;500;600;700&display=swap">
<style>
  :root {
    --ink: #111111;
    --text: #3a3a3a;
    --muted: #8a8a8a;
    --accent: #ec2f35;
    --rule: #e4e4e4;
    --tag: #e9e9e9;
    --panel: #f1f1f1;
    --black: #050505;
    --white: #ffffff;
  }
  * { box-sizing: border-box; margin: 0; padding: 0; }
  html, body { width: 693px; height: 1200px; overflow: hidden; background: var(--white); }
  body { position: relative; font-family: "Figtree", Arial, sans-serif; color: var(--text); }

  .topbar { position: absolute; top: 0; left: 0; width: 693px; height: 28px; background: var(--black); }
  .brand { position: absolute; left: 80px; top: 5px; display: flex; align-items: center; gap: 5px; color: var(--white); font-weight: 700; font-size: 15px; line-height: 18px; }
  .brand-mark { width: 13px; height: 13px; border: 2px solid var(--white); border-radius: 2px; }

  .hero { position: absolute; top: 28px; left: 0; width: 693px; height: 113px; display: flex; }
  .hero-photo { height: 100%; }
  .hero-photo.ruins { width: 182px; background: linear-gradient(160deg, #2a5fa8 0%, #6f8cb0 40%, #b48a2e 70%, #5a4214 100%); }
  .hero-photo.festival { width: 79px; background: linear-gradient(180deg, #c13a6a 0%, #e0a0a8 50%, #b5324f 100%); }
  .hero-photo.river { width: 78px; background: linear-gradient(180deg, #6f7a48 0%, #44522c 50%, #c8a13a 85%, #b5465a 100%); }
  .hero-photo.study { width: 186px; background: linear-gradient(180deg, #9a9a9a 0%, #5c5c5c 55%, #3b3b3b 100%); }
  .hero-photo.patrol { width: 168px; background: linear-gradient(150deg, #6a8ab0 0%, #3a4654 45%, #8a5530 80%, #4a2a18 100%); }

  .intro { position: absolute; top: 167px; left: 0; width: 693px; text-align: center; }
  .intro h1 { font-size: 15px; font-weight: 500; color: var(--ink); line-height: 20px; }
  .intro p { margin-top: 4px; font-size: 9.5px; color: var(--ink); letter-spacing: 0.2px; }

  .rule { position: absolute; left: 79px; width: 531px; height: 1px; background: var(--rule); }
  .rule.one { top: 214px; }
  .rule.two { top: 404px; }

  .videos-title { position: absolute; top: 228px; left: 0; width: 693px; text-align: center; font-size: 12px; font-weight: 500; color: var(--accent); }
  .view-all { position: absolute; top: 232px; right: 83px; font-size: 7px; font-style: italic; color: var(--ink); text-decoration: underline; display: flex; align-items: center; gap: 3px; }

  .video { position: absolute; top: 266px; width: 124px; text-align: center; }
  .video.uploader { left: 118px; }
  .video.publishing { left: 279px; }
  .video.galleries { left: 439px; }
  .thumb { position: relative; width: 124px; height: 81px; }
  .thumb.worker { background: linear-gradient(160deg, #d8e0d4 0%, #6a7a48 45%, #8a5a2a 75%, #4e5a38 100%); }
  .thumb.billboard { background: linear-gradient(180deg, #6a6f72 0%, #5a6c88 40%, #2e4a7a 65%, #4a463c 100%); }
  .thumb.archway { background: linear-gradient(160deg, #2a5fa8 0%, #7a8cb0 35%, #c09030 65%, #6a4c18 100%); }
  .thumb svg { position: absolute; left: 42px; top: 20px; }
  .video h3 { margin-top: 9px; font-size: 9px; font-weight: 500; line-height: 12px; color: var(--accent); }

  .faq { position: absolute; top: 418px; left: 79px; width: 358px; }
  .faq > h2 { font-size: 12px; font-weight: 500; color: var(--accent); margin-left: -1px; }
  .faq-item { height: 125px; padding-top: 13px; border-bottom: 1px solid var(--rule); }
  .faq-item:first-of-type { padding-top: 11px; }
  .faq-item:last-of-type { border-bottom: none; }
  .faq-item h3 { font-size: 9.5px; font-weight: 600; line-height: 12px; color: var(--ink); }
  .faq-item p { margin-top: 5px; font-size: 7.6px; line-height: 12px; color: var(--text); }
  .tags { margin-top: 6px; display: flex; align-items: center; gap: 5px; font-size: 7.6px; color: var(--ink); }
  .tags span.tag { background: var(--tag); border-radius: 6px; padding: 1px 6px; }

  .load-more { position: absolute; top: 1067px; left: 76px; width: 360px; height: 24px; background: var(--panel); color: var(--accent); font-size: 9.5px; line-height: 24px; text-align: center; }

  .sidebar { position: absolute; top: 418px; left: 467px; width: 140px; }
  .sidebar h2 { font-size: 12px; font-weight: 500; color: var(--accent); }
  .search { margin-top: 9px; display: flex; margin-left: -1px; }
  .search-field { width: 107px; height: 19px; border: 1px solid var(--rule); font-size: 7px; font-style: italic; color: var(--muted); padding: 5px 5px; }
  .search-button { width: 20px; height: 19px; background: var(--accent); display: flex; align-items: center; justify-content: center; }
  .featured { margin-top: 20px; }
  .sidebar ul { list-style: none; margin-top: 8px; }
  .featured li { position: relative; padding-left: 11px; font-size: 7.6px; line-height: 12px; color: var(--ink); margin-bottom: 4.5px; width: 130px; }
  .categories { margin-top: 17px; }
  .categories li { position: relative; padding-left: 11px; font-size: 7.6px; line-height: 14px; color: var(--ink); }
  .sidebar li::before { content: ""; position: absolute; left: 1px; top: 4px; width: 4px; height: 4px; border-radius: 50%; background: var(--accent); }

  .live-help { position: absolute; left: 674px; top: 272px; width: 19px; height: 73px; background: #1d1d1d; border-radius: 3px 0 0 3px; }
  .live-help span { position: absolute; left: 3px; top: 11px; writing-mode: vertical-rl; font-size: 7.5px; color: var(--white); font-weight: 500; }
  .live-help i { position: absolute; left: 6px; top: 56px; width: 7px; height: 6px; background: var(--white); border-radius: 50%; }

  .footer { position: absolute; top: 1131px; left: 0; width: 693px; height: 69px; background: var(--black); text-align: center; }
  .footer-links { margin-top: 14px; font-size: 6.2px; color: #cfa878; word-spacing: 1px; }
  .footer-links b { color: #777; font-weight: 400; margin: 0 4px; }
  .copyright { margin-top: 9px; font-size: 6.2px; font-weight: 700; color: var(--white); }
  .powered { margin-top: 2px; font-size: 6px; color: #777; }
</style>
</head>
<body>
  <header class="topbar">
    <div class="brand"><span class="brand-mark"></span>BrightKestrel</div>
  </header>

  <section class="hero">
    <div class="hero-photo ruins" role="img" aria-label="Photo of sunlit stone ruins with an archway under a blue sky"></div>
    <div class="hero-photo festival" role="img" aria-label="Photo of a child in a colourful festival headdress"></div>
    <div class="hero-photo river" role="img" aria-label="Photo of a boat laden with flowers on a river"></div>
    <div class="hero-photo study" role="img" aria-label="Black and white photo of a man seated in a study"></div>
    <div class="hero-photo patrol" role="img" aria-label="Photo of uniformed officers standing beside a villager"></div>
  </section>

  <section class="intro">
    <h1>BrightKestrel Support Center</h1>
    <p>Resources to provide you wiht additional insight into the worls of Photography</p>
  </section>
  <div class="rule one"></div>

  <h2 class="videos-title">Latest Video Tutorials</h2>
  <a class="view-all">View all Videos
    <svg width="4" height="5" viewBox="0 0 4 5"><path d="M0 0 L4 2.5 L0 5 Z" fill="#111"/></svg>
  </a>

  <article class="video uploader">
    <div class="thumb worker" role="img" aria-label="Video still of a farm worker with a wheelbarrow">
      <svg width="40" height="40" viewBox="0 0 40 40"><circle cx="20" cy="20" r="18.5" fill="rgba(255,255,255,0.15)" stroke="#fff" stroke-width="1.5"/><path d="M15 11 L29 20 L15 29 Z" fill="#fff"/></svg>
    </div>
    <h3>Uploading Files Using the Drag and Drop Uploader</h3>
  </article>
  <article class="video publishing">
    <div class="thumb billboard" role="img" aria-label="Video still of a large painted billboard by a road">
      <svg width="40" height="40" viewBox="0 0 40 40"><circle cx="20" cy="20" r="18.5" fill="rgba(255,255,255,0.15)" stroke="#fff" stroke-width="1.5"/><path d="M15 11 L29 20 L15 29 Z" fill="#fff"/></svg>
    </div>
    <h3>Publishing Files</h3>
  </article>
  <article class="video galleries">
    <div class="thumb archway" role="img" aria-label="Video still of stone ruins with an archway">
      <svg width="40" height="40" viewBox="0 0 40 40"><circle cx="20" cy="20" r="18.5" fill="rgba(255,255,255,0.15)" stroke="#fff" stroke-width="1.5"/><path d="M15 11 L29 20 L15 29 Z" fill="#fff"/></svg>
    </div>
    <h3>Creating Galleries</h3>
  </article>

  <div class="rule two"></div>

  <main class="faq">
    <h2>Frecuent Asked Questions (F.A.Q)</h2>
    <article class="faq-item">
      <h3>Lorem ipsum dolor sit amet, consectetur adipisicing elit, sed do eiusmod tempor incididunt ut labore?</h3>
      <p>Et dolore magna aliqua. Ut enim ad minim veniam, quis nostrud exercitation ullamco laboris nisi ut aliquip ex ea commodo consequat. Duis aute irure dolor in reprehenderit in voluptate velit esse cillum dolore eu fugiat nulla pariatur. Excepteur sint occaecat cupidatat non proident, sunt in culpa qui officia deserunt mollit anim id est laborum.</p>
      <div class="tags">Category:&nbsp; <span class="tag">Photo</span><span class="tag">Beginer</span><span class="tag">Billing</span><span class="tag">Other</span></div>
    </article>
    <article class="faq-item">
      <h3>Lorem ipsum dolor sit amet, consectetur adipisicing elit, sed do eiusmod tempor incididunt ut labore?</h3>
      <p>Et dolore magna aliqua. Ut enim ad minim veniam, quis nostrud exercitation ullamco laboris nisi ut aliquip ex ea commodo consequat. Duis aute irure dolor in reprehenderit in voluptate velit esse cillum dolore eu fugiat nulla pariatur. Excepteur sint occaecat cupidatat non proident, sunt in culpa qui officia deserunt mollit anim id est laborum.</p>
      <div class="tags">Category:&nbsp; <span class="tag">Photo</span><span class="tag">Beginer</span><span class="tag">Billing</span><span class="tag">Other</span></div>
    </article>
    <article class="faq-item">
      <h3>Lorem ipsum dolor sit amet, consectetur adipisicing elit, sed do eiusmod tempor incididunt ut labore?</h3>
      <p>Et dolore magna aliqua. Ut enim ad minim veniam, quis nostrud exercitation ullamco laboris nisi ut aliquip ex ea commodo consequat. Duis aute irure dolor in reprehenderit in voluptate velit esse cillum dolore eu fugiat nulla pariatur. Excepteur sint occaecat cupidatat non proident, sunt in culpa qui officia deserunt mollit anim id est laborum.</p>
      <div class="tags">Category:&nbsp; <span class="tag">Photo</span><span class="tag">Beginer</span><span class="tag">Billing</span><span class="tag">Other</span></div>
    </article>
    <article class="faq-item">
      <h3>Lorem ipsum dolor sit amet, consectetur adipisicing elit, sed do eiusmod tempor incididunt ut labore?</h3>
      <p>Et dolore magna aliqua. Ut enim ad minim veniam, quis nostrud exercitation ullamco laboris nisi ut aliquip ex ea commodo consequat. Duis aute irure dolor in reprehenderit in voluptate velit esse cillum dolore eu fugiat nulla pariatur. Excepteur sint occaecat cupidatat non proident, sunt in culpa qui officia deserunt mollit anim id est laborum.</p>
      <div class="tags">Category:&nbsp; <span class="tag">Photo</span><span class="tag">Beginer</span><span class="tag">Billing</span><span class="tag">Other</span></div>
    </article>
    <article class="faq-item">
      <h3>Lorem ipsum dolor sit amet, consectetur adipisicing elit, sed do eiusmod tempor incididunt ut labore?</h3>
      <p>Et dolore magna aliqua. Ut enim ad minim veniam, quis nostrud exercitation ullamco laboris nisi ut aliquip ex ea commodo consequat. Duis aute irure dolor in reprehenderit in voluptate velit esse cillum dolore eu fugiat nulla pariatur. Excepteur sint occaecat cupidatat non proident, sunt in culpa qui officia deserunt mollit anim id est laborum.</p>
      <div class="tags">Category:&nbsp; <span class="tag">Photo</span><span class="tag">Beginer</span><span class="tag">Billing</span><span class="tag">Other</span></div>
    </article>
  </main>

  <div class="load-more">Load More Questions</div>

  <aside class="sidebar">
    <h2>Search</h2>
    <div class="search">
      <div class="search-field">Type your search...</div>
      <div class="search-button">
        <svg width="11" height="11" viewBox="0 0 11 11"><circle cx="4.6" cy="4.6" r="3.4" fill="none" stroke="#fff" stroke-width="1.5"/><path d="M7 7 L10 10" stroke="#fff" stroke-width="1.6" stroke-linecap="round"/></svg>
      </div>
    </div>
    <section class="featured">
      <h2>Featured Articles</h2>
      <ul>
        <li>Why I can't login into my account?</li>
        <li>How to Upload batch images into your account</li>
        <li>Why I can't login into my account?</li>
        <li>How to Upload batch images into your account</li>
      </ul>
    </section>
    <section class="categories">
      <h2>Categories</h2>
      <ul>
        <li>Assets Managment (2)</li>
        <li>Beginners (9)</li>
        <li>Bug (1)</li>
        <li>Billing (7)</li>
        <li>Content (3)</li>
        <li>Gallery (2)</li>
        <li>Photo Uploading (3)</li>
        <li>Pro (1)</li>
        <li>Publishing (3)</li>
      </ul>
    </section>
  </aside>

  <div class="live-help"><span>Live Help</span><i></i></div>

  <footer class="footer">
    <div class="footer-links">Home<b>•</b>Contact Us<b>•</b>Affiliate Program<b>•</b>Privacy Policy<b>•</b>Site Terms and Conditions<b>•</b>About Us</div>
    <div class="copyright">© Copyright 2014 Northvale Images Pte Ltd. All rights reserved.</div>
    <div class="powered">Powered by BrightKestrel</div>
  </footer>
</body>
</html>
```